Apartment services app

The app should permit current residents to pay rent, submit work orders or submit comments and general requests. There is an app that is available from Heron Works in the UK that could be used to benchmark, but I would like to see something more appropriate for the US.
Updates

The company name for this project is Oakvale Property Management. We will be providing a logo at a later date as we we will be submitting a separate design project for the development of a new logo.

Reason: I am extending the deadline by another week so that I may comment on the designs so far and each of you will have time to respond Tim

Target Market(s)

Residents of our apartment communities

Industry/Entity Type

Apartment

Requirements
Must have
• Ability to pay rent
• Ability to have reminders sent to resident
• Notices sent to resident
• Resident able to submit work order requests
• Resident able to submit comments and complaints

```html
<!DOCTYPE html>
<html lang="en">
<head>
<meta charset="utf-8">
<title>Oakvale Property Management – Resident App Screens</title>
<link href="https://fonts.googleapis.com/css2?family=Roboto:wght@300;400;500&family=Roboto+Condensed:wght@300&display=swap" rel="stylesheet">
<style>
  :root {
    --page-bg: #ffffff;
    --header-top: #4a95b6;
    --header-bottom: #3a86a8;
    --header-text: #ffffff;
    --screen-top: #f2f2f2;
    --screen-bottom: #ebebeb;
    --accent: #1f6d93;
    --name-text: #1d1d1d;
    --field-bg: #fafafa;
    --placeholder: #a9a9a9;
    --caret: #4a6cd8;
    --button-bg: #0d6a90;
    --button-text: #ffffff;
  }
  * { box-sizing: border-box; margin: 0; padding: 0; }
  html, body {
    width: 1200px;
    height: 1000px;
    overflow: hidden;
    background: var(--page-bg);
    font-family: "Roboto", "Helvetica Neue", Arial, sans-serif;
  }
  .canvas {
    position: relative;
    width: 1200px;
    height: 1000px;
  }
  .screen {
    position: absolute;
    top: 147px;
    width: 402px;
    height: 713px;
    background: linear-gradient(180deg, var(--screen-top), var(--screen-bottom));
    overflow: hidden;
  }
  .screen--message { left: 115px; }
  .screen--programs { left: 673px; }

  .app-header {
    position: absolute;
    top: 0; left: 0;
    width: 100%;
    height: 43px;
    background: linear-gradient(180deg, var(--header-top), var(--header-bottom));
    color: var(--header-text);
    display: flex;
    align-items: center;
  }
  .back-link {
    position: absolute;
    left: 12px;
    top: 0;
    height: 43px;
    display: flex;
    align-items: center;
    gap: 5px;
    font-size: 19px;
    font-weight: 300;
  }
  .back-link svg { width: 15px; height: 24px; }
  .app-title {
    position: absolute;
    top: 0;
    height: 43px;
    line-height: 45px;
    font-size: 17px;
    font-weight: 300;
    letter-spacing: 0.2px;
    text-transform: uppercase;
  }
  .screen--message .app-title { left: 132px; }
  .screen--programs .app-title { left: 98px; }

  .recipient {
    position: absolute;
    left: 12px;
    top: 56px;
  }
  .recipient-role {
    font-family: "Roboto Condensed", "Roboto", sans-serif;
    font-weight: 300;
    font-size: 29px;
    line-height: 32px;
    color: var(--accent);
    letter-spacing: -0.3px;
  }
  .recipient-name {
    font-size: 17px;
    font-weight: 400;
    color: var(--name-text);
    line-height: 20px;
  }

  .field {
    position: absolute;
    left: 12px;
    width: 376px;
    background: var(--field-bg);
    color: var(--placeholder);
    font-weight: 300;
    font-size: 19px;
  }
  .field--line {
    top: 144px;
    height: 42px;
    line-height: 44px;
    padding-left: 12px;
  }
  .field--line::before {
    content: "";
    position: absolute;
    left: 9px;
    top: 3px;
    width: 2px;
    height: 30px;
    background: var(--caret);
  }
  .field--area {
    top: 199px;
    height: 159px;
    padding: 12px 12px;
    line-height: 24px;
  }

  .primary-button {
    position: absolute;
    left: 12px;
    top: 370px;
    width: 376px;
    height: 63px;
    background: var(--button-bg);
    color: var(--button-text);
    font-size: 21px;
    font-weight: 500;
    display: flex;
    align-items: center;
    justify-content: center;
    box-shadow: 2px 2px 3px rgba(0, 0, 0, 0.3);
  }
</style>
</head>
<body>
<main class="canvas">

  <section class="screen screen--message" aria-label="Send message screen">
    <header class="app-header">
      <span class="back-link">
        <svg viewBox="0 0 15 24" aria-hidden="true"><path d="M12 2 L3 12 L12 22" fill="none" stroke="#ffffff" stroke-width="3" stroke-linecap="round" stroke-linejoin="round"/></svg>
        Back
      </span>
      <h1 class="app-title">Send Message</h1>
    </header>
    <div class="recipient">
      <p class="recipient-role">Manager</p>
      <p class="recipient-name">Dana Whitcomb</p>
    </div>
    <div class="field field--line">Subject</div>
    <div class="field field--area">Input message</div>
    <div class="primary-button">Send Message</div>
  </section>

  <section class="screen screen--programs" aria-label="Volunteer programs screen">
    <header class="app-header">
      <span class="back-link">
        <svg viewBox="0 0 15 24" aria-hidden="true"><path d="M12 2 L3 12 L12 22" fill="none" stroke="#ffffff" stroke-width="3" stroke-linecap="round" stroke-linejoin="round"/></svg>
        Back
      </span>
      <h1 class="app-title">Volunteer Programs</h1>
    </header>
    <div class="recipient">
      <p class="recipient-role">Manager</p>
      <p class="recipient-name">Dana Whitcomb</p>
    </div>
    <div class="field field--line">Program Name</div>
    <div class="field field--area">Program details</div>
    <div class="primary-button">List Program</div>
  </section>

</main>
</body>
</html>
```